Dental website design - brightmolarhouse.net

We are looking to do a redesign for the website: brightmolarhouse.net

Please use Sections from this google Slide I created: https://slides.vantoreplan.net/deck/8kQwZr2LmNpT5vXyA7cB3dEf9GhJ0sUiVo/edit#page=id.p

Target Market(s)

Dentistry

Industry/Entity Type

Dental Clinic

Number of Pages Required

1 page

Colors
f68e4e
86cae7

Requirements
Must have
• Please use Sections from this google Slide I created: https://slides.vantoreplan.net/deck/8kQwZr2LmNpT5vXyA7cB3dEf9GhJ0sUiVo/edit#page=id.p

```html
<!DOCTYPE html>
<html lang="en">
<head>
<meta charset="utf-8">
<title>Bright Molar House – Dental Care</title>
<link href="https://fonts.googleapis.com/css2?family=Lora:ital,wght@0,600;0,700;1,400&family=Open+Sans:wght@400;600&family=Montserrat:wght@500;600;700&display=swap" rel="stylesheet">
<style>
  :root{
    --orange:#f68e4e;
    --orange-deep:#e8772f;
    --sky:#86cae7;
    --navy:#1e3765;
    --ink:#3a3f4a;
    --muted:#6f7582;
    --mist:#eef0f3;
    --white:#ffffff;
  }
  *{box-sizing:border-box;margin:0;padding:0}
  html,body{width:1200px;height:2328px;overflow:hidden;background:var(--white)}
  body{font-family:"Open Sans",Arial,sans-serif;color:var(--ink);position:relative}

  /* header */
  .site-header{position:absolute;top:0;left:0;width:1200px;height:112px;background:var(--white);box-shadow:0 2px 6px rgba(0,0,0,.06);z-index:2}
  .brand{position:absolute;left:36px;top:32px;display:flex;align-items:center;gap:12px}
  .brand-dot{width:38px;height:38px;border-radius:50%;background:var(--sky)}
  .brand-name{font-family:"Montserrat",sans-serif;font-weight:700;font-size:15px;color:var(--navy);letter-spacing:.3px}
  .top-contact{position:absolute;right:24px;top:10px;display:flex;gap:28px;font-size:11px;color:var(--muted);align-items:center}
  .top-contact span{display:flex;align-items:center;gap:6px}
  .main-nav{position:absolute;left:286px;top:64px;display:flex;gap:18px;font-family:"Montserrat",sans-serif;font-size:10px;font-weight:600;color:var(--navy);white-space:nowrap}
  .nav-cta{position:absolute;left:1026px;top:40px;width:84px;height:72px;background:var(--orange-deep);color:var(--white);font-family:"Montserrat",sans-serif;font-weight:700;font-size:11px;display:flex;align-items:center;justify-content:center}

  /* hero */
  .hero{position:absolute;top:112px;left:0;width:1200px;height:480px}
  .hero-photo{position:absolute;inset:0;background:linear-gradient(100deg,#f3ede8 0%,#eee2dc 32%,#d99a94 55%,#b8575a 72%,#e9d6cf 100%)}
  .hero-copy{position:absolute;left:108px;top:56px;width:560px}
  .hero-title{font-family:"Lora",serif;font-weight:700;font-size:42px;line-height:1.15;color:var(--navy)}
  .hero-sub{margin-top:16px;font-size:13px;line-height:1.6;color:var(--ink);width:300px}
  .btn{display:inline-block;background:var(--orange-deep);color:var(--white);font-family:"Montserrat",sans-serif;font-weight:600;font-size:11px;letter-spacing:.5px;padding:14px 22px}
  .hero .btn{margin-top:36px}

  /* about */
  .about{position:absolute;top:592px;left:0;width:1200px;height:640px;background:var(--mist)}
  .section-title{font-family:"Lora",serif;font-weight:700;color:var(--navy);text-align:center}
  .about .section-title{font-size:24px;margin-top:46px}
  .title-rule{width:260px;height:1px;background:#c9cdd4;margin:10px auto 0}
  .about-text{width:780px;margin:30px auto 0;text-align:center;font-size:13px;line-height:1.85;color:var(--muted)}
  .about-text p+p{margin-top:24px}
  .learn-more{display:block;text-align:center;margin-top:36px;font-family:"Lora",serif;font-weight:600;font-size:15px;color:var(--navy)}
  .tools-art{position:absolute;left:0;top:300px;width:200px;height:250px;background:linear-gradient(150deg,#c3c8cf,#8d949e);border-radius:0 60px 60px 0;opacity:.7}
  .tooth-art{position:absolute;left:870px;top:270px;width:250px;height:230px;background:radial-gradient(circle at 45% 45%,#ffffff 0%,#eef6fb 55%,#cfe7f3 100%);border-radius:40px}

  /* mission */
  .mission{position:absolute;top:1232px;left:0;width:1200px;height:688px;background:var(--white)}
  .mission-copy{position:absolute;left:140px;top:70px;width:360px}
  .mission .section-title{text-align:left;font-size:22px}
  .mission .title-rule{margin:10px 0 0;width:120px}
  .mission-text{margin-top:40px;font-size:12px;line-height:1.7;color:var(--muted)}
  .mission-text p+p{margin-top:16px}
  .social{display:flex;gap:22px;margin-top:40px}
  .social span{width:22px;height:22px;border-radius:50%;background:var(--navy)}
  .mission .btn{margin-top:32px}
  .mission-photo{position:absolute;left:580px;top:0;width:620px;height:688px;background:linear-gradient(160deg,#f1eef4 0%,#e4dced 40%,#c9b6d6 75%,#b9a3c9 100%)}

  /* testimonials */
  .testimonials{position:absolute;top:1920px;left:0;width:1200px;height:408px;background:var(--white)}
  .testimonials .section-title{font-size:30px;margin-top:30px}
  .testimonials .title-rule{width:820px;margin-top:14px}
  .quote{width:860px;margin:36px auto 0;text-align:center;font-family:"Lora",serif;font-style:italic;font-size:14px;line-height:1.9;color:var(--ink)}
  .arrow{position:absolute;top:210px}
  .arrow.prev{left:140px}
  .arrow.next{right:140px}
</style>
</head>
<body>

<header class="site-header">
  <div class="brand"><span class="brand-dot"></span><span class="brand-name">Bright Molar House</span></div>
  <div class="top-contact">
    <span><svg width="10" height="13" viewBox="0 0 10 13"><path d="M5 0a5 5 0 0 0-5 5c0 3.5 5 8 5 8s5-4.5 5-8a5 5 0 0 0-5-5zm0 7a2 2 0 1 1 0-4 2 2 0 0 1 0 4z" fill="#6f7582"/></svg>1820 Harbor Crest Avenue, Lakeview, CA 90210</span>
    <span><svg width="12" height="12" viewBox="0 0 12 12"><path d="M2.5 0.5l2 2.5-1.2 1.5a7 7 0 0 0 4.2 4.2L9 7.5l2.5 2-1.5 2C5 11.5.5 7 .5 2z" fill="#6f7582"/></svg>(555) 214-0937</span>
  </div>
  <nav class="main-nav">
    <span>PREVENTATIVE CARE ▾</span>
    <span>GET IN TOUCH ▾</span>
    <span>PATIENT INFORMATION ▾</span>
    <span>DENTAL IMPLANTS ▾</span>
    <span>RESTORATIVE DENTISTRY ▾</span>
  </nav>
  <div class="nav-cta">CONTACT ▾</div>
</header>

<section class="hero">
  <div class="hero-photo" role="img" aria-label="Close-up photo of a smile with a dental mirror and probe"></div>
  <div class="hero-copy">
    <h1 class="hero-title">Cosmetic Dentistry for a<br>Dazzling New Smile</h1>
    <p class="hero-sub">Gentle, modern care that brings out the best in your smile every day.</p>
    <a class="btn">GET IN TOUCH</a>
  </div>
</section>

<section class="about">
  <div class="tools-art" role="img" aria-label="Illustration of dental instruments"></div>
  <div class="tooth-art" role="img" aria-label="Illustration of cheerful tooth characters"></div>
  <h2 class="section-title">About Bright Molar House</h2>
  <div class="title-rule"></div>
  <div class="about-text">
    <p>At our practice we believe a healthy smile starts with trust. Our team listens closely, explains every option in plain words and plans treatment around your goals, your schedule and your comfort. From routine cleanings to complete smile makeovers, we bring careful hands, modern tools and a calm setting to every single visit you make with us.</p>
    <p>Families across the valley have relied on our dentists for years. We offer same week appointments, clear pricing before any work begins and friendly reminders so nothing is missed. Whether you need a quick check or a full restoration, we are here to help you feel confident and cared for.</p>
  </div>
  <a class="learn-more">Learn more</a>
</section>

<section class="mission">
  <div class="mission-copy">
    <h2 class="section-title">Our Mission</h2>
    <div class="title-rule"></div>
    <div class="mission-text">
      <p>To be the trusted home for dental care in our community, serving every patient with warmth.</p>
      <p>To treat each person with honesty and respect, using proven methods and modern technology to protect healthy teeth for life.</p>
      <p>To make every visit easy, from booking to follow up, in a relaxed and welcoming setting.</p>
      <p>To keep learning and growing so our patients always receive thoughtful, high quality and lasting results.</p>
    </div>
    <div class="social"><span></span><span></span><span></span><span></span></div>
    <a class="btn">Book an appointment</a>
  </div>
  <div class="mission-photo" role="img" aria-label="Photo of a patient in a dental chair during an examination"></div>
</section>

<section class="testimonials">
  <h2 class="section-title">What our Patients are Saying</h2>
  <div class="title-rule"></div>
  <p class="quote">From the first phone call I felt welcome. I had put off a visit for years because I was nervous, but the whole team was patient and kind. They explained each step, kept me comfortable and my new crown looks completely natural. Booking was simple, the office is spotless and they even checked in the next day. I finally look forward to my checkups and my whole family now goes here too. Thank you to everyone at the front desk and in the chair for making such a difference, I would recommend this practice to anyone looking for honest and caring dentists.</p>
  <svg class="arrow prev" width="14" height="22" viewBox="0 0 14 22"><path d="M12 2L3 11l9 9" stroke="#1e3765" stroke-width="3" fill="none"/></svg>
  <svg class="arrow next" width="14" height="22" viewBox="0 0 14 22"><path d="M2 2l9 9-9 9" stroke="#1e3765" stroke-width="3" fill="none"/></svg>
</section>

</body>
</html>
```